Willowmere Therapy (Endure - Renew - Flourish) - Double Sided Business Card

I would like a 2-sided business card. Front: Matte Black or Navy with Logo & Tagline. Back: Name, Address, Phone Number, Email, & Website (maybe would like to include a small map pin-pointing location); Prefer front to be a gold/silver foil (iridescent); Back prefer white or light colored background with lettering that is easy to read and simple

Target Market(s)

Individuals & Couples (13 y.o. - ALL Adults); High end clientele

Industry/Entity Type

Licensed Professional Counselor (Mental Health)

Contact Information for Business Card

Name: Willowmere Therapy; Tagline: Endure - Renew - Flourish; Address: 3175 W. Calder Ave., Suite 842, Fort Worth, TX 76142; Phone: (214) 738-2956; Website: www.WillowmereTherapy.example

Font styles to use
Serif

Requirements
Must have
• Logo on Front (Large) prefer gold/silver foil on a matte dark color (i.e. black, navy, etc.); Back of Card: All other relevant information

```html
<!DOCTYPE html>
<html lang="en">
<head>
<meta charset="utf-8">
<title>Willowmere Therapy – Business Card</title>
<link rel="stylesheet" href="https://fonts.googleapis.com/css2?family=Cinzel:wght@400;600&display=swap">
<style>
  :root {
    --backdrop: #9d9891;
    --card: #1d1c1d;
    --gold: #d8b23c;
    --silver: #8f8f94;
    --ink-light: #f2f0ec;
  }
  * { margin: 0; padding: 0; box-sizing: border-box; }
  html, body {
    width: 1200px; height: 900px; overflow: hidden;
    background: var(--backdrop);
    font-family: "Cinzel", "Times New Roman", serif;
  }
  .stage {
    width: 1200px; height: 900px;
    display: flex; flex-direction: column;
    align-items: center; justify-content: center; gap: 56px;
  }
  .card {
    position: relative;
    width: 660px; height: 378px;
    background: var(--card);
    border-radius: 14px;
    box-shadow: 0 10px 24px rgba(0,0,0,.25);
    color: var(--gold);
  }

  /* Front */
  .card-front .brand {
    position: absolute; top: 110px; left: 0; right: 0;
    display: flex; flex-direction: column; align-items: center; gap: 18px;
  }
  .brand-mark {
    width: 58px; height: 58px; border-radius: 50%;
    background: var(--gold);
  }
  .brand-name {
    font-size: 38px; font-weight: 600; letter-spacing: 2px;
    color: var(--gold); text-transform: uppercase;
  }
  .brand-rule {
    width: 250px; height: 2px; background: var(--silver);
  }
  .card-front .tagline {
    position: absolute; bottom: 48px; left: 0; right: 0;
    text-align: center; font-size: 16px; letter-spacing: 1.5px;
    text-transform: uppercase;
  }

  /* Back */
  .card-back .back-mark {
    position: absolute; top: 46px; left: 292px;
    width: 76px; height: 76px; border-radius: 50%;
    background: var(--gold);
  }
  .card-back .identity {
    position: absolute; left: 46px; bottom: 54px;
    text-align: right;
  }
  .identity .name {
    font-size: 27px; font-weight: 600; line-height: 1.2;
    color: var(--gold);
  }
  .identity .tagline {
    margin-top: 8px; font-size: 13px; letter-spacing: .5px;
  }
  .contact-list {
    position: absolute; left: 320px; top: 170px;
    list-style: none;
    display: flex; flex-direction: column; gap: 22px;
  }
  .contact-item {
    display: flex; align-items: center; gap: 22px;
    color: var(--ink-light); font-size: 15px; line-height: 1.25;
  }
  .contact-item svg {
    width: 20px; height: 20px; flex: none;
    stroke: var(--gold); fill: none; stroke-width: 1.6;
  }
</style>
</head>
<body>
<main class="stage">
  <section class="card card-front" aria-label="Card front">
    <div class="brand">
      <span class="brand-mark" aria-hidden="true"></span>
      <span class="brand-name">Willowmere Therapy</span>
      <span class="brand-rule" aria-hidden="true"></span>
    </div>
    <p class="tagline">Endure - Renew - Flourish</p>
  </section>

  <section class="card card-back" aria-label="Card back">
    <span class="back-mark" aria-hidden="true"></span>
    <div class="identity">
      <p class="name">Willowmere<br>Therapy</p>
      <p class="tagline">Endure - Renew - Flourish</p>
    </div>
    <ul class="contact-list">
      <li class="contact-item">
        <svg viewBox="0 0 24 24" aria-hidden="true"><path d="M12 22s7-7.2 7-12.5A7 7 0 0 0 5 9.5C5 14.8 12 22 12 22z"/><circle cx="12" cy="9.5" r="2.5"/></svg>
        <span>3175 W. Calder Ave., Suite 842,<br>Fort Worth, TX 76142</span>
      </li>
      <li class="contact-item">
        <svg viewBox="0 0 24 24" aria-hidden="true"><path d="M5 3h4l2 5-2.5 1.5a11 11 0 0 0 6 6L16 13l5 2v4a2 2 0 0 1-2 2A17 17 0 0 1 3 5a2 2 0 0 1 2-2z"/></svg>
        <span>(214) 738-2956</span>
      </li>
      <li class="contact-item">
        <svg viewBox="0 0 24 24" aria-hidden="true"><circle cx="12" cy="12" r="9"/><path d="M3 12h18M12 3c3 3.5 3 14.5 0 18M12 3c-3 3.5-3 14.5 0 18"/></svg>
        <span>www.WillowmereTherapy.example</span>
      </li>
    </ul>
  </section>
</main>
</body>
</html>
```